Startup photography business has a new logo, now we need business cards

Design a business card for the two partners of our business.
Our business Brisk Pelican has a new logo and we need to design a business card to showcase it and us.
Our colours of blue and orange are punchy and vivid, but how can we make the most of it on our card?

It should have our name Brisk Pelican
name of partner
phone number
email
website

Industry/Entity Type

Professional Photography

Contact Information for Business Card

Tom Ashworth
+61 400 55 61 72
tom@briskpelican.com.au
briskpelican.com.au

second card
Neil Porter
+61 400 918 263
neil@briskpelican.com.au
briskpelican.com.au

Colors
f37122
f68d4c
33a6d7
0592cd

Requirements
Must have
• one version of our logo, we have included options
• Name
• phone number
• email
• website
Nice to have
• instagram briskpelicanmedia
• twitter briskpelicanmedia
• facebook briskpelicanmedia

```html
<!DOCTYPE html>
<html lang="en">
<head>
<meta charset="utf-8">
<title>Brisk Pelican — Business Cards</title>
<link href="https://fonts.googleapis.com/css2?family=Source+Sans+3:wght@400;600;700&display=swap" rel="stylesheet">
<style>
  :root {
    --brand-blue: #33a6d7;
    --brand-blue-deep: #0592cd;
    --card-white: #ffffff;
    --ink: #1c1c1c;
    --backdrop: #ecebe9;
  }
  * { box-sizing: border-box; margin: 0; padding: 0; }
  html, body {
    width: 1200px;
    height: 900px;
    overflow: hidden;
    background: var(--backdrop);
    font-family: "Source Sans 3", "Myriad Pro", Arial, sans-serif;
  }
  .stage { position: relative; width: 1200px; height: 900px; }

  .card {
    position: absolute;
    overflow: hidden;
    box-shadow: 0 6px 18px rgba(0,0,0,0.18);
  }

  /* Front: contact card */
  .card--front {
    left: 238px; top: 62px;
    width: 555px; height: 343px;
    background: var(--brand-blue);
  }
  .front-mark {
    position: absolute;
    left: -8px; top: 6px;
    width: 330px; height: 330px;
    border-radius: 50%;
    background: var(--card-white);
    display: flex; align-items: center; justify-content: center;
  }
  .front-mark__name {
    color: var(--brand-blue);
    font-weight: 700;
    font-size: 34px;
    letter-spacing: 0.5px;
  }
  .contact {
    position: absolute;
    right: 26px; top: 118px;
    color: var(--card-white);
    text-align: right;
  }
  .contact__name {
    font-weight: 600;
    font-size: 18px;
    margin-bottom: 34px;
    margin-right: 0;
  }
  .contact__list { list-style: none; }
  .contact__item {
    display: flex; justify-content: flex-end; align-items: center;
    gap: 8px;
    font-size: 14.5px;
    line-height: 20px;
  }
  .contact__icon { width: 11px; height: 11px; flex: none; }

  /* Back: logo card */
  .card--back {
    left: 457px; top: 518px;
    width: 560px; height: 344px;
    background: var(--card-white);
  }
  .back-mark {
    position: absolute;
    left: 0; right: 0; top: 110px;
    display: flex; flex-direction: column; align-items: center; gap: 26px;
  }
  .back-mark__dot {
    width: 84px; height: 84px;
    border-radius: 50%;
    background: var(--brand-blue);
  }
  .back-mark__name {
    color: var(--brand-blue);
    font-weight: 700;
    font-size: 40px;
    letter-spacing: 1px;
    text-transform: uppercase;
  }
</style>
</head>
<body>
<main class="stage">

  <section class="card card--front" aria-label="Business card front">
    <div class="front-mark">
      <span class="front-mark__name">Brisk Pelican</span>
    </div>
    <div class="contact">
      <p class="contact__name">Tom Ashworth</p>
      <ul class="contact__list">
        <li class="contact__item">+61 400 55 61 72
          <svg class="contact__icon" viewBox="0 0 12 12" aria-hidden="true"><path fill="#fff" d="M2.4 0.6l2 2.2-1 1.3c.7 1.6 2 2.9 3.6 3.6l1.3-1 2.2 2-1.1 2.4C5.3 11 1 6.7.1 2.3z"/></svg>
        </li>
        <li class="contact__item">tom@briskpelican.com.au
          <svg class="contact__icon" viewBox="0 0 12 12" aria-hidden="true"><rect x="0.5" y="2" width="11" height="8" fill="#fff"/><path d="M0.8 2.5L6 6.6l5.2-4.1" stroke="#33a6d7" stroke-width="1" fill="none"/></svg>
        </li>
        <li class="contact__item">briskpelican.com.au
          <svg class="contact__icon" viewBox="0 0 12 12" aria-hidden="true"><circle cx="6" cy="6" r="5.5" fill="#fff"/><path d="M0.8 6h10.4M6 0.6c-2.4 2.8-2.4 8 0 10.8M6 0.6c2.4 2.8 2.4 8 0 10.8" stroke="#33a6d7" stroke-width="0.9" fill="none"/></svg>
        </li>
      </ul>
    </div>
  </section>

  <section class="card card--back" aria-label="Business card back">
    <div class="back-mark">
      <span class="back-mark__dot"></span>
      <span class="back-mark__name">Brisk Pelican</span>
    </div>
  </section>

</main>
</body>
</html>
```